QUORVEL_sci fi poster design

poster design for an independent film about the creation of the world's first "perfect" artificial intelligence. we have an idea of the direction but are open to new ideas.
Film is titled "Quorvel"
It is a sparse film. Three actors in one location. dialog driven, thinking person's sci-fi film.
so a simple design could work well.

Synopsis:
Martin Oszlo is a prodigy roboticist that has been at work for the past decade creating Tobin, an advanced artificial intelligence indistinguishable from a human. Beth Collier is the reporter given an exclusive week of access to interview them. As she and Martin grow closer during their week together, the robot exhibits startling Open State in the form of jealousy and anger. As relationships between all three parties reach a boiling point, secrets are revealed and technology is both revered and reviled.

Attached is a concept that we like.
we do not like the font and the actual artwork -- just the concept. does not feel sophisticated enough or "cool" enough.

Another idea would be to incorporate the idea of the "Quorvel Valley" (graph included with attached documents)
http://en.lorepedix.org/wiki/Uncanny_valley

we have screen caps from the film but the resolution is not very high. I will enclose a few in case they are of use.

credit block is enclosed in photoshop file with font

ADDED SOME DESIGNS FROM SIMILAR THEMED FILMS THAT WE LIKE.

we need it in standard film poster size and resolution 27" x 40".

new conceptual ideas posted in the directions as well as in attachments. thanks

sophisticated science fiction fans.

Work

• You can include the following actors names above the title (in the design):
Glen Torvald
Nora Pemberley

```html
<!DOCTYPE html>
<html lang="en">
<head>
<meta charset="utf-8">
<title>Quorvel — Film Poster</title>
<link rel="stylesheet" href="https://fonts.googleapis.com/css2?family=Raleway:wght@200;300;400&family=Oswald:wght@300;400&display=swap">
<style>
  :root {
    --ink: #000000;
    --paper: #f2f2f2;
    --text: #e6e6e6;
    --muted: #a8a8a8;
    --faint: #7a7a7a;
    --scene-light: #e9e9e9;
    --scene-mid: #8c8c8c;
  }
  html, body {
    margin: 0;
    padding: 0;
    width: 811px;
    height: 1200px;
    overflow: hidden;
    background: var(--ink);
  }
  .poster {
    position: relative;
    width: 811px;
    height: 1200px;
    background: var(--ink);
    color: var(--text);
    font-family: "Raleway", sans-serif;
  }
  .cast {
    position: absolute;
    top: 10px;
    left: 0;
    width: 100%;
    text-align: center;
    font-family: "Oswald", sans-serif;
    font-weight: 300;
    font-size: 11px;
    letter-spacing: 2.4px;
    color: var(--muted);
  }
  .cast .sep { margin: 0 8px; }
  .scene {
    position: absolute;
    top: 40px;
    left: 96px;
    width: 620px;
    height: 730px;
    background:
      linear-gradient(to bottom, rgba(0,0,0,0) 62%, rgba(0,0,0,0.85) 82%, var(--ink) 100%),
      linear-gradient(to right, var(--scene-light) 0%, var(--scene-light) 44%, #111 44.5%, #111 53.5%, var(--scene-light) 54%, var(--scene-light) 100%);
  }
  .credit-director {
    position: absolute;
    top: 742px;
    left: 0;
    width: 100%;
    text-align: center;
    font-weight: 300;
    font-size: 12px;
    letter-spacing: 3.5px;
    color: var(--muted);
  }
  .title {
    position: absolute;
    top: 792px;
    left: 0;
    width: 100%;
    margin: 0;
    text-align: center;
    font-weight: 200;
    font-size: 62px;
    letter-spacing: 18px;
    padding-left: 18px;
    box-sizing: border-box;
    color: var(--paper);
  }
  .billing {
    position: absolute;
    top: 1062px;
    left: 190px;
    width: 431px;
    text-align: center;
    font-family: "Oswald", sans-serif;
    font-weight: 300;
    font-size: 8px;
    line-height: 12px;
    letter-spacing: 0.6px;
    color: var(--muted);
  }
  .billing p { margin: 0; }
  .site {
    position: absolute;
    top: 1148px;
    left: 0;
    width: 100%;
    text-align: center;
    font-family: "Oswald", sans-serif;
    font-weight: 300;
    font-size: 8px;
    letter-spacing: 0.8px;
    color: var(--faint);
  }
</style>
</head>
<body>
  <main class="poster">
    <header class="cast">
      GLEN TORVALD<span class="sep">|</span>EVAN HALLOWAY PRYCE<span class="sep">|</span>NORA PEMBERLEY
    </header>

    <div class="scene" role="img" aria-label="Black and white film still: two men seated across a chess board at a railing, silhouetted against two tall bright windows patterned with circuitry, divided by a dark pillar"></div>

    <p class="credit-director">DIRECTED BY SIMON ACHTERBERG</p>

    <h1 class="title">QUORVEL</h1>

    <section class="billing">
      <p>HARBORLINE PICTURES PRESENTS AN OPEN STATE / FIELD LINE PRODUCTIONS IN ASSOCIATION WITH NORTHGATE ENTERTAINMENT</p>
      <p>“QUORVEL” GLEN TORVALD NORA PEMBERLEY EVAN HALLOWAY PRYCE ORIGINAL SCORE BY ROSS KEMBER EDITED BY SIMON ACHTERBERG</p>
      <p>PRODUCTION DESIGNER LENA VARGO DANA MILLS PETER ORLAND PRODUCED BY JON AVERY WRITTEN BY SHAWN CARDELL DIRECTED BY SIMON ACHTERBERG</p>
    </section>

    <p class="site">www.fieldlinefilms.com</p>
  </main>
</body>
</html>
```